Awesome Beer Labels for food pairing

We are going to launch a range of craft beers specially brewed for food pairing, and we are in need of a logo and bottle labels to represent this. Every label individually has to show which beer type it is and the food groups it matches with. At the same time the whole range has to have the same appearance as we are promoting it as a whole package. As we are targeting middle-high to high class hospitality businesses we are looking for a luxurious, exclusive feel to the labels. We also need room for a clear title of the beer and a small food pairing description.

Industry/Entity Type

Craft Brewery

Font styles to use
Sans Serif
Decorative
Script

Colors

Designer to choose colors to be used in the design.

Requirements
Must have
• -Different beer labels where the style and name of the beer comes first, and the beer type second
• - A logo for the whole group which also has to be printed on glasses, so nothing to detailed.
• - Clear, recognizable pictures, drawings or symbols for the different food groups.
• - Room for the name of the beer, the beer type and a small description.
Nice to have
• An exclusive, luxurious look and feel that would not stand out in an high class restaurant.
• Something that combines the whole range of beers (something like a overlaying or connecting picture that combines alle the labels?)
Should not have
• To much different styles, the beers have to match

```html
<!DOCTYPE html>
<html lang="en">
<head>
<meta charset="utf-8">
<title>Craft Beer Label</title>
<link rel="stylesheet" href="https://fonts.googleapis.com/css2?family=Playfair+Display:wght@400;500&family=Pinyon+Script&family=IM+Fell+English:ital@0;1&display=swap">
<style>
  :root {
    --backdrop: #c3c3c6;
    --label-cream: #f9f2e3;
    --brand-red: #d9381e;
    --ray-beige: #eadfbd;
    --cheese-yellow: #f2c230;
    --pepper-red: #c8281c;
  }
  * { margin: 0; padding: 0; box-sizing: border-box; }
  html, body {
    width: 1200px; height: 800px; overflow: hidden;
    background: var(--backdrop);
  }
  .canvas { position: relative; width: 1200px; height: 800px; }
  .label {
    position: absolute; left: 325px; top: 30px;
    width: 520px; height: 700px;
    transform: scale(1.057); transform-origin: top left;
    background: radial-gradient(circle at 50% 50%, var(--ray-beige) 0%, var(--label-cream) 55%);
    box-shadow: 10px 10px 14px rgba(0,0,0,0.35);
    color: var(--brand-red);
    font-family: "Playfair Display", serif;
    text-align: center;
  }
  .label-frame { position: absolute; inset: 0; width: 520px; height: 700px; }
  .brand {
    position: absolute; left: 0; right: 0; top: 160px;
    display: flex; align-items: center; justify-content: center; gap: 10px;
    font-size: 28px; font-weight: 400; line-height: 1;
  }
  .brand-dot { width: 14px; height: 14px; border-radius: 50%; background: var(--brand-red); }
  .craft { position: absolute; left: 0; right: 0; top: 240px; font-size: 52px; line-height: 1; }
  .beer-name { position: absolute; left: 0; right: 0; top: 300px; font-size: 112px; font-weight: 400; line-height: 1; letter-spacing: 2px; }
  .beer-type { position: absolute; left: 0; right: 0; top: 418px; font-family: "Pinyon Script", cursive; font-size: 40px; line-height: 1; font-weight: 700; }
  .pairing-note {
    position: absolute; left: 70px; right: 70px; top: 487px;
    font-family: "IM Fell English", serif; font-size: 13px; line-height: 17px;
  }
  .food-icons {
    position: absolute; left: 210px; top: 532px; width: 104px; height: 54px;
    border-radius: 12px;
    background: linear-gradient(90deg, var(--cheese-yellow) 0 55%, var(--pepper-red) 55% 100%);
  }
  .net-volume { position: absolute; left: 0; right: 0; top: 652px; font-size: 20px; line-height: 1; }
</style>
</head>
<body>
<main class="canvas">
  <section class="label">
    <svg class="label-frame" viewBox="0 0 520 700" aria-hidden="true">
      <path fill="none" stroke="var(--brand-red)" stroke-width="7" stroke-linejoin="round"
        d="M75,92 Q170,80 240,80 Q255,78 260,66 Q265,78 280,80 Q350,80 445,92
           Q450,118 478,124 Q485,220 490,320 Q492,340 512,352 Q492,364 490,384
           Q485,480 478,578 Q450,584 445,608 Q350,620 280,620 Q265,622 260,638
           Q255,622 240,620 Q170,620 75,608 Q70,584 42,578 Q35,480 30,384
           Q28,364 8,352 Q28,340 30,320 Q35,220 42,124 Q70,118 75,92 Z"/>
    </svg>
    <div class="brand"><span class="brand-dot"></span><span class="brand-name">Hartwell Ale</span></div>
    <p class="craft">Craft</p>
    <h1 class="beer-name">BEER</h1>
    <p class="beer-type">beer type</p>
    <p class="pairing-note">Lorem ipsum dolor sit amet, consectetur adipiscing elit,<br>sed do eiusmod tempor incididunt ut labore et dolore</p>
    <div class="food-icons" role="img" aria-label="Food pairing icons: a wedge of cheese and a red chili pepper"></div>
    <p class="net-volume">Nt.Wt. 160 ml</p>
  </section>
</main>
</body>
</html>
```